Business Card design for an International Import Export House

We need a Business Card design for our import export business. We trade in Minerals, Metals, Rice, Sugar, Steel etc.. The design should be minimalistic. It may or may not contain the physical address. In case you want to include the physical address - 418 Verandah Heights, Marlow Sector 9, Gurgaon, Haryana, India, 122009.

Target Market(s)

Steel Mills or Steel Plants, Factories, Mining businesses, Industrial houses, Government Agencies

Industry/Entity Type

Importer

Contact Information for Business Card

Business Name - Tessan Overseas

Font styles to use
Other font styles liked:
• montserrat

Requirements
Must have
• Ravi Kandola - President
• www.tessanoverseas.com
• ravi@tessanoverseas.com
• +91-987-654-3217
Nice to have
• worldwide suppliers of ores

```html
<!DOCTYPE html>
<html lang="en">
<head>
<meta charset="UTF-8">
<title>Tessan Overseas — Business Card</title>
<link rel="stylesheet" href="https://fonts.googleapis.com/css2?family=Montserrat:wght@400;500;700&display=swap">
<style>
  :root {
    --teal: #3f8fa6;
    --teal-soft: #5aa6bb;
    --charcoal: #1f2427;
    --white: #ffffff;
    --stage: #e6e8e9;
  }
  * { margin: 0; padding: 0; box-sizing: border-box; }
  html, body {
    width: 1200px;
    height: 900px;
    overflow: hidden;
    background: var(--stage);
    font-family: "Montserrat", Arial, sans-serif;
  }
  .sheet {
    width: 1200px;
    height: 900px;
    display: flex;
    align-items: center;
    justify-content: center;
    gap: 40px;
  }
  .card {
    position: relative;
    width: 540px;
    height: 309px;
    overflow: hidden;
    box-shadow: 0 6px 18px rgba(0,0,0,0.18);
  }

  /* Front */
  .card-front { background: var(--white); }
  .brand-mark {
    position: absolute;
    left: 118px;
    top: 56px;
    width: 96px;
    height: 96px;
    border-radius: 50%;
    background: var(--teal);
  }
  .brand-name {
    position: absolute;
    left: 36px;
    top: 182px;
    font-weight: 700;
    font-size: 24px;
    letter-spacing: 0.5px;
    text-transform: uppercase;
    color: var(--teal);
    white-space: nowrap;
  }
  .globe-art {
    position: absolute;
    right: -40px;
    top: 40px;
    width: 250px;
    height: 300px;
    border-radius: 50% 0 0 50%;
    background: radial-gradient(circle at 40% 45%, var(--teal-soft), var(--teal));
  }

  /* Back */
  .card-back { background: var(--charcoal); }
  .back-band { position: absolute; inset: 0; }
  .holder {
    position: absolute;
    left: 30px;
    top: 26px;
    color: var(--white);
  }
  .holder-name { font-size: 17px; font-weight: 500; letter-spacing: 0.5px; }
  .holder-role { font-size: 12px; font-weight: 400; margin-top: 3px; }
  .contact-list {
    position: absolute;
    right: 30px;
    bottom: 28px;
    width: 330px;
    list-style: none;
    font-size: 13px;
    line-height: 1.5;
    color: var(--teal-soft);
  }
  .contact-list li {
    display: flex;
    justify-content: flex-end;
    align-items: center;
    gap: 14px;
    text-align: right;
    margin-top: 4px;
  }
  .contact-dot {
    flex: none;
    width: 9px;
    height: 9px;
    border-radius: 50%;
    border: 1.5px solid var(--white);
  }
</style>
</head>
<body>
  <main class="sheet">
    <section class="card card-front" aria-label="Card front">
      <span class="brand-mark"></span>
      <span class="brand-name">Tessan Overseas</span>
      <div class="globe-art" role="img" aria-label="Illustrated globe showing continents in teal"></div>
    </section>

    <section class="card card-back" aria-label="Card back">
      <svg class="back-band" width="540" height="309" viewBox="0 0 540 309" aria-hidden="true">
        <polygon points="0,0 540,0 540,20 300,135 0,135" fill="var(--teal)"/>
      </svg>
      <div class="holder">
        <p class="holder-name">Ravi Kandola</p>
        <p class="holder-role">President</p>
      </div>
      <ul class="contact-list">
        <li><span>+91-987-654-3217</span><span class="contact-dot"></span></li>
        <li><span>www.tessanoverseas.com<br>ravi@tessanoverseas.com</span><span class="contact-dot"></span></li>
        <li><span>418 Verandah Heights, Marlow Sector 9,<br>Dunmere, Kestrel Vale, 560231</span><span class="contact-dot"></span></li>
      </ul>
    </section>
  </main>
</body>
</html>
```